Square Business Cards for Our Restaurant / Event Venue

We need square business cards designed for the management team of our event venue and restaurant. On one side of the card should be the the Harbor Lantern 7 logo and URL www.harborlantern7.example. On the other side should be the Ember Logo and URL www.emberhall7.example. All employee details should be on the side with Ember logo. There will be a total of 5 cards to be created with the design.

Clara Bennquist
clara@harborlantern7.example

main 555.418.3072
direct 555.730.2946

4831 West Orchard Lane SE
Washington, DC 90417

Industry/Entity Type

Business

```html
<!DOCTYPE html>
<html lang="en">
<head>
<meta charset="utf-8">
<title>Harbor Lantern 7 / Ember — Business Cards</title>
<link href="https://fonts.googleapis.com/css2?family=Arimo:wght@400;700&display=swap" rel="stylesheet">
<style>
  :root {
    --backdrop: #9a9a9a;
    --card-white: #f7f7f7;
    --card-black: #0c0c0c;
    --brand-red: #b81f25;
    --ink: #1a1a1a;
    --ink-soft: #3a3a3a;
    --rule: #a8a8a8;
  }
  * { margin: 0; padding: 0; box-sizing: border-box; }
  html, body { width: 1200px; height: 900px; overflow: hidden; }
  body {
    background: var(--backdrop);
    font-family: "Arimo", Arial, sans-serif;
    position: relative;
  }
  .card {
    position: absolute;
    left: 250px;
    width: 700px;
    height: 400px;
    border-radius: 22px;
    overflow: hidden;
    box-shadow: 0 10px 28px rgba(0,0,0,0.35);
  }

  /* Back side */
  .card-back { top: 40px; background: var(--card-black); }
  .back-mark {
    position: absolute;
    left: 250px; top: 70px;
    width: 200px; height: 200px;
    border-radius: 50%;
    background: var(--brand-red);
    display: flex; align-items: center; justify-content: center;
  }
  .back-name {
    color: var(--card-black);
    font-size: 26px;
    font-weight: 400;
    text-align: center;
    line-height: 1.15;
  }
  .back-url {
    position: absolute;
    left: 0; right: 0; top: 305px;
    text-align: center;
    color: #ffffff;
    font-size: 17px;
    letter-spacing: 0.3px;
  }

  /* Front side */
  .card-front { top: 460px; background: var(--card-white); }
  .front-brand {
    position: absolute;
    left: 70px; top: 95px;
    font-size: 68px;
    font-weight: 700;
    color: var(--ink);
    letter-spacing: -1px;
  }
  .person {
    position: absolute;
    right: 60px; top: 100px;
    text-align: right;
  }
  .person-name {
    color: var(--brand-red);
    font-size: 31px;
    font-weight: 700;
  }
  .person-title {
    color: var(--ink-soft);
    font-size: 21px;
    margin-top: 4px;
  }
  .person-rule {
    position: absolute;
    left: 330px; right: 60px; top: 182px;
    height: 1px;
    background: var(--rule);
  }
  .address {
    position: absolute;
    right: 60px; top: 205px;
    text-align: right;
    color: var(--ink);
    font-size: 16px;
    line-height: 1.35;
  }
  .contact-rule {
    position: absolute;
    left: 40px; top: 262px;
    width: 290px; height: 1px;
    background: var(--rule);
  }
  .contacts {
    position: absolute;
    left: 40px; top: 272px;
    list-style: none;
    font-size: 16px;
    color: var(--ink);
  }
  .contacts li {
    display: flex; align-items: center;
    height: 23px;
  }
  .contacts svg { width: 14px; height: 14px; margin-right: 9px; flex: none; }
  .front-band {
    position: absolute;
    left: 0; bottom: 0;
    width: 700px; height: 26px;
  }
</style>
</head>
<body>

  <section class="card card-back" aria-label="Card back">
    <div class="back-mark">
      <span class="back-name">Harbor<br>Lantern 7</span>
    </div>
    <p class="back-url">www.harborlantern7.example</p>
  </section>

  <section class="card card-front" aria-label="Card front">
    <div class="front-brand">Ember</div>

    <div class="person">
      <div class="person-name">Clara Bennquist</div>
      <div class="person-title">Managing Director</div>
    </div>
    <div class="person-rule"></div>

    <div class="address">
      4831 West Orchard Lane SE<br>
      Washington, DC 90417
    </div>

    <div class="contact-rule"></div>
    <ul class="contacts">
      <li>
        <svg viewBox="0 0 24 24" aria-hidden="true"><path fill="#b81f25" d="M6.6 10.8a15.1 15.1 0 0 0 6.6 6.6l2.2-2.2c.3-.3.7-.4 1-.2 1.1.4 2.3.6 3.6.6.6 0 1 .4 1 1V20c0 .6-.4 1-1 1A17 17 0 0 1 3 4c0-.6.4-1 1-1h3.5c.6 0 1 .4 1 1 0 1.3.2 2.5.6 3.6.1.3 0 .7-.2 1z"/></svg>
        555.418.3072
      </li>
      <li>
        <svg viewBox="0 0 24 24" aria-hidden="true"><rect x="6" y="2" width="12" height="20" rx="2" fill="none" stroke="#b81f25" stroke-width="2"/><circle cx="12" cy="18" r="1.2" fill="#b81f25"/></svg>
        555.730.2946
      </li>
      <li>
        <svg viewBox="0 0 24 24" aria-hidden="true"><rect x="2" y="5" width="20" height="14" rx="1" fill="#b81f25"/><path d="M2 6l10 7 10-7" fill="none" stroke="#f7f7f7" stroke-width="1.6"/></svg>
        clara@harborlantern7.example
      </li>
      <li>
        <svg viewBox="0 0 24 24" aria-hidden="true"><circle cx="12" cy="12" r="9.5" fill="none" stroke="#b81f25" stroke-width="2"/><ellipse cx="12" cy="12" rx="4" ry="9.5" fill="none" stroke="#b81f25" stroke-width="1.6"/><path d="M2.5 12h19M4 7h16M4 17h16" stroke="#b81f25" stroke-width="1.4"/></svg>
        www.emberhall7.example
      </li>
    </ul>

    <svg class="front-band" viewBox="0 0 700 26" preserveAspectRatio="none" aria-hidden="true">
      <polygon points="0,10 470,10 462,26 0,26" fill="var(--card-black)"/>
      <polygon points="482,0 700,0 700,26 470,26" fill="var(--brand-red)"/>
    </svg>
  </section>

</body>
</html>
```